" Trata-se de uma construtora em conjunto com um escritório de engenharia e arquitetura para prestar serviços de construção, gerenciamento de obras e projetos e desenho. "

```html
<!DOCTYPE html>
<html lang="pt-BR">
<head>
<meta charset="utf-8">
<title>Vértice — Construção e gerenciamento de Obras</title>
<link rel="stylesheet" href="https://fonts.googleapis.com/css2?family=Open+Sans:wght@300;400;600;700&display=swap">
<style>
  :root{
    --stage:#e8e8e6;
    --ink:#ffffff;
    --ink-soft:rgba(255,255,255,.72);
    --ink-faint:rgba(255,255,255,.45);
    --gold:#d4a640;
    --shade:rgba(20,18,16,.55);
    --panel:#f4f2ee;
    --panel-ink:#3a3632;
  }
  *{box-sizing:border-box;margin:0;padding:0}
  html,body{width:1200px;height:1200px;overflow:hidden}
  body{background:var(--stage);font-family:"Open Sans",sans-serif;color:var(--ink);position:relative}

  .screen{position:absolute;overflow:hidden;background:#2b2724}
  .hero-photo{position:absolute;inset:0;
    background:
      radial-gradient(ellipse at 70% 30%, rgba(230,220,205,.55) 0%, rgba(230,220,205,0) 45%),
      linear-gradient(160deg,#8d8377 0%,#5f574e 35%,#3a342e 65%,#24201c 100%)}
  .hero-tint{position:absolute;inset:0;background:linear-gradient(90deg,rgba(15,13,11,.55) 0%,rgba(15,13,11,.15) 60%,rgba(15,13,11,.3) 100%)}

  /* desktop */
  .desktop{left:40px;top:40px;width:1120px;height:630px}
  .nav{position:absolute;top:26px;right:40px;display:flex;align-items:center;gap:26px;font-size:12px;font-weight:600;letter-spacing:.04em}
  .nav a{color:var(--ink);text-decoration:none}
  .nav .menu-icon{width:20px;height:14px}
  .headline{position:absolute;left:96px;top:235px}
  .headline .lead{font-weight:300;font-size:30px;line-height:1.25}
  .headline .title{font-weight:700;font-size:34px;line-height:1.25}
  .actions{position:absolute;left:96px;top:345px;display:flex;align-items:center;gap:34px}
  .btn-more{font-size:12px;font-weight:600;letter-spacing:.12em;padding-bottom:8px;border-bottom:2px solid var(--gold);width:140px}
  .btn-video{display:flex;align-items:center;gap:10px;font-size:11px;font-weight:600;letter-spacing:.08em}
  .btn-video svg{width:30px;height:30px}
  .chat{position:absolute;right:110px;top:430px;width:250px;background:var(--shade);border:1px solid rgba(255,255,255,.15);padding:14px 16px;font-size:11px}
  .chat .who{display:flex;align-items:center;gap:10px;margin-bottom:10px}
  .chat .avatar{width:26px;height:26px;border-radius:50%;background:#b89a72}
  .chat .who b{font-weight:600;display:block}
  .chat .who span{color:var(--ink-soft)}
  .chat .reply{display:flex;justify-content:space-between;align-items:center;color:var(--ink-faint);border-top:1px solid rgba(255,255,255,.15);padding-top:8px}
  .chat .reply i{width:14px;height:14px;background:var(--ink);display:block}
  .footer-bar{position:absolute;left:0;right:0;bottom:0;height:54px;border-top:1px solid rgba(255,255,255,.12);display:flex;align-items:center;padding:0 96px;gap:120px;font-size:10px;letter-spacing:.1em;color:var(--ink-soft)}
  .footer-bar b{color:var(--gold);font-weight:600}

  /* mobile */
  .mobile{left:495px;top:705px;width:210px;height:455px;border-radius:22px}
  .mobile .brand{position:absolute;top:26px;left:0;right:0;text-align:center;font-weight:600;font-size:15px;letter-spacing:.18em}
  .mobile .mnav{position:absolute;top:62px;left:16px;right:16px;display:flex;gap:12px;font-size:8px;font-weight:600}
  .mobile .mnav .bar{margin-left:auto;width:12px;height:8px;border-top:2px solid var(--gold);border-bottom:2px solid var(--gold)}
  .mobile .mhead{position:absolute;left:0;right:0;top:200px;text-align:center;font-size:15px;line-height:1.3}
  .mobile .mhead .lead{font-weight:300}
  .mobile .mhead .title{font-weight:700}
  .mobile .mactions{position:absolute;left:18px;right:18px;bottom:22px;display:flex;justify-content:space-between;align-items:center;font-size:7px;font-weight:600;letter-spacing:.1em}
  .mobile .mactions .btn-more{width:64px;font-size:7px;padding-bottom:5px}
  .mobile .mactions svg{width:18px;height:18px}
</style>
</head>
<body>

<section class="screen desktop">
  <div class="hero-photo" role="img" aria-label="Sala de estar moderna com paredes de concreto aparente, sofá claro e claraboia"></div>
  <div class="hero-tint"></div>

  <nav class="nav">
    <a href="#">Home</a>
    <a href="#">Quem somos</a>
    <a href="#">Obras</a>
    <svg width="14" height="14" viewBox="0 0 14 14" fill="none" stroke="#fff" stroke-width="1.6"><circle cx="6" cy="6" r="4.5"/><path d="M9.5 9.5 13 13"/></svg>
    <svg class="menu-icon" viewBox="0 0 20 14" stroke="var(--gold)" stroke-width="2"><path d="M0 1h20M6 7h14M0 13h20"/></svg>
  </nav>

  <div class="headline">
    <p class="lead">Seja bem vindo ao novo conceito de</p>
    <p class="title">Construção e gerenciamento de Obras</p>
  </div>

  <div class="actions">
    <span class="btn-more">SAIBA MAIS</span>
    <span class="btn-video">
      <svg viewBox="0 0 30 30" fill="none"><circle cx="15" cy="15" r="14" stroke="#fff" stroke-width="1.2"/><path d="M12 10l8 5-8 5z" fill="#fff"/></svg>
      VEJA O VÍDEO
    </span>
  </div>

  <aside class="chat">
    <div class="who"><span class="avatar"></span><div><b>Fale conosco</b><span>Como podemos ajudar hoje?</span></div></div>
    <div class="reply">Digite sua mensagem<i></i></div>
  </aside>

  <div class="footer-bar">
    <span>DESLIZE PARA <b>CONHECER</b></span>
    <span>01</span><span>02</span><span>03</span>
  </div>
</section>

<section class="screen mobile">
  <div class="hero-photo" role="img" aria-label="Interior residencial com concreto aparente e luz natural"></div>
  <div class="hero-tint"></div>
  <div class="brand">VÉRTICE</div>
  <nav class="mnav"><span>Home</span><span>Quem somos</span><span>Obras</span><span class="bar"></span></nav>
  <div class="mhead">
    <p class="lead">Seja bem vindo<br>ao novo conceito de</p>
    <p class="title">Construção e<br>gerenciamento<br>de Obras</p>
  </div>
  <div class="mactions">
    <span class="btn-more">SAIBA MAIS</span>
    <svg viewBox="0 0 30 30" fill="none"><circle cx="15" cy="15" r="14" stroke="#fff" stroke-width="1.5"/><path d="M12 10l8 5-8 5z" fill="#fff"/></svg>
  </div>
</section>

</body>
</html>
```